Field Trip Flyer

We need a flyer to promote our field trips. I would like the flyer to be bright, eye popping and modern. We offer STEM Field Trips as well for an educational opportunity that connects roller skating and STEM concepts. We offer field trips for 2 or 3 hours and all field trips include skating, skate rental, play zone, arcade games available, concessions available, + much more! Field trips are fun, unique and engaging and can be booked online at brindlewavefun.com. Our business name is Brindlewave Skate Center. The flyer design needs to be front and back.

Target Market(s)

Elementary School Teachers

Requirements
Must have
• Front and Back Design, 5.5 x 8.5,Field Trip Inclusions: Skating, skate rental, play zone, arcade available, concessions available + much more!, STEM Field Trips available, book online at brindlewavefun.com
Nice to have
• engaging key words to describe the field trips
Should not have
• too much words or irrelevant information

```html
<!DOCTYPE html>
<html lang="en">
<head>
<meta charset="utf-8">
<title>Brindlewave Skate Center – Field Trip Flyer</title>
<link rel="stylesheet" href="https://fonts.googleapis.com/css2?family=Rubik:wght@500;700;800&family=Oswald:wght@500&display=swap">
<style>
  :root {
    --royal: #3340c4;
    --royal-deep: #2630a8;
    --red: #e8173f;
    --red-burst: #e3242b;
    --ink: #2b2b2b;
    --white: #ffffff;
    --page: #efefef;
  }
  html, body {
    margin: 0;
    padding: 0;
    width: 1200px;
    height: 2342px;
    overflow: hidden;
    background: var(--page);
  }
  .canvas {
    position: relative;
    width: 1200px;
    height: 2342px;
  }
  .flyer {
    position: absolute;
    left: 50px;
    top: 459px;
    width: 1100px;
    height: 1424px;
    box-shadow: 0 18px 40px rgba(0,0,0,0.28);
    background: var(--white);
  }
  .flyer svg { display: block; }
  .headline { font-family: "Rubik", sans-serif; font-weight: 700; fill: var(--white); font-size: 44px; }
  .offer-title { font-family: "Rubik", sans-serif; font-weight: 700; font-size: 40px; }
  .offer-line { font-family: "Rubik", sans-serif; font-weight: 700; font-size: 22px; fill: var(--ink); }
  .accent { fill: var(--red); }
  .bubble-text { font-family: "Rubik", sans-serif; font-weight: 700; font-size: 23px; fill: var(--red); }
  .inclusion { font-family: "Rubik", sans-serif; font-weight: 500; font-size: 23px; fill: var(--ink); }
  .burst-text { font-family: "Rubik", sans-serif; font-weight: 700; font-size: 21px; fill: var(--white); }
  .brand-name { font-family: "Rubik", sans-serif; font-weight: 700; font-size: 15px; fill: var(--royal-deep); }
  .booking { font-family: "Oswald", sans-serif; font-weight: 500; font-size: 13.5px; fill: var(--white); }
</style>
</head>
<body>
<div class="canvas">
  <div class="flyer">
    <svg width="1100" height="1424" viewBox="0 0 717 928" xmlns="http://www.w3.org/2000/svg">
      <defs>
        <linearGradient id="crowd-tone" x1="0" y1="0" x2="1" y2="1">
          <stop offset="0" stop-color="#c9a27a"/>
          <stop offset="0.5" stop-color="#6a5a78"/>
          <stop offset="1" stop-color="#3b4aa8"/>
        </linearGradient>
        <linearGradient id="playzone-tone" x1="0" y1="0" x2="0" y2="1">
          <stop offset="0" stop-color="#8a6c8e"/>
          <stop offset="0.6" stop-color="#c9b7a6"/>
          <stop offset="1" stop-color="#3aa64a"/>
        </linearGradient>
        <linearGradient id="rink-tone" x1="0" y1="0" x2="0" y2="1">
          <stop offset="0" stop-color="#e7c24a"/>
          <stop offset="0.45" stop-color="#9fb6e0"/>
          <stop offset="1" stop-color="#d9e4f2"/>
        </linearGradient>
      </defs>

      <!-- blue upper field -->
      <rect class="top-field" x="0" y="0" width="717" height="520" fill="var(--royal)"/>

      <!-- curved divider -->
      <path class="divider-red" d="M0,470 Q250,410 520,500 L717,490 L717,520 L0,520 Z" fill="var(--red)"/>
      <path class="lower-field" d="M0,482 Q250,422 520,512 L717,500 L717,928 L0,928 Z" fill="var(--white)"/>

      <!-- brand mark -->
      <g class="brand">
        <circle cx="115" cy="115" r="65" fill="var(--white)"/>
        <text class="brand-name" x="115" y="111" text-anchor="middle">Brindlewave</text>
        <text class="brand-name" x="115" y="130" text-anchor="middle">Skate Center</text>
      </g>

      <!-- main photo -->
      <circle cx="536" cy="220" r="256" fill="var(--white)"/>
      <clipPath id="main-photo-clip"><circle cx="536" cy="220" r="250"/></clipPath>
      <g role="img" aria-label="Photo of smiling schoolchildren gathered at the skate center counter" clip-path="url(#main-photo-clip)">
        <rect x="280" y="-40" width="460" height="520" fill="url(#crowd-tone)"/>
      </g>

      <!-- headline cloud -->
      <g class="headline-cloud" fill="var(--red)">
        <rect x="0" y="245" width="300" height="140" rx="20"/>
        <circle cx="70" cy="250" r="48"/>
        <circle cx="170" cy="245" r="50"/>
        <circle cx="265" cy="265" r="50"/>
        <circle cx="305" cy="325" r="52"/>
        <circle cx="270" cy="380" r="42"/>
        <circle cx="160" cy="395" r="40"/>
        <circle cx="55" cy="390" r="38"/>
      </g>
      <text class="headline" x="69" y="277">We offer</text>
      <text class="headline" x="69" y="325">STEM</text>
      <text class="headline" x="69" y="373">Field Trips</text>

      <!-- offer block -->
      <text class="offer-title" x="50" y="505" fill="var(--ink)">We <tspan class="accent">offer</tspan></text>
      <g class="clock-icon" fill="none" stroke="var(--red)" stroke-width="3">
        <circle cx="63" cy="532" r="11"/>
        <path d="M63,525 V532 L68,535"/>
      </g>
      <text class="offer-line" x="89" y="540">field trips for <tspan class="accent">2 or 3 hours</tspan></text>

      <!-- speech bubble -->
      <path class="bubble" d="M68,558 H276 Q305,558 305,586 Q305,614 276,614 H230 L215,648 L205,614 H68 Q40,614 40,586 Q40,558 68,558 Z"
            fill="var(--white)" stroke="var(--royal)" stroke-width="3.5"/>
      <text class="bubble-text" x="172" y="595" text-anchor="middle">All field trips include</text>

      <!-- inclusions -->
      <g class="inclusions">
        <g transform="translate(58,665)">
          <circle r="10" fill="var(--royal)"/><path d="M-5,0 L-1,4 L5,-4" fill="none" stroke="#fff" stroke-width="2.5"/>
        </g>
        <text class="inclusion" x="79" y="673">skating</text>
        <g transform="translate(58,703)">
          <circle r="10" fill="var(--royal)"/><path d="M-5,0 L-1,4 L5,-4" fill="none" stroke="#fff" stroke-width="2.5"/>
        </g>
        <text class="inclusion" x="79" y="711">skate rental</text>
        <g transform="translate(58,740)">
          <circle r="10" fill="var(--royal)"/><path d="M-5,0 L-1,4 L5,-4" fill="none" stroke="#fff" stroke-width="2.5"/>
        </g>
        <text class="inclusion" x="79" y="748">play zone</text>
        <g transform="translate(58,778)">
          <circle r="10" fill="var(--royal)"/><path d="M-5,0 L-1,4 L5,-4" fill="none" stroke="#fff" stroke-width="2.5"/>
        </g>
        <text class="inclusion" x="79" y="786">arcade</text>
        <g transform="translate(58,815)">
          <circle r="10" fill="var(--royal)"/><path d="M-5,0 L-1,4 L5,-4" fill="none" stroke="#fff" stroke-width="2.5"/>
        </g>
        <text class="inclusion" x="79" y="823">games available</text>
      </g>

      <!-- starburst -->
      <polygon class="burst" fill="var(--red-burst)"
        points="485,730 461.6,755.9 468.9,790 435.7,800.7 425,833.9 390.9,826.6 365,850 339.1,826.6 305,833.9 294.3,800.7 261.1,790 268.4,755.9 245,730 268.4,704.1 261.1,670 294.3,659.3 305,626.1 339.1,633.4 365,610 390.9,633.4 425,626.1 435.7,659.3 468.9,670 461.6,704.1"/>
      <text class="burst-text" x="365" y="697" text-anchor="middle">concessions</text>
      <text class="burst-text" x="365" y="724" text-anchor="middle">available,</text>
      <text class="burst-text" x="365" y="751" text-anchor="middle">+</text>
      <text class="burst-text" x="365" y="779" text-anchor="middle">much more!</text>

      <!-- small photos -->
      <circle cx="592" cy="522" r="108" fill="var(--white)"/>
      <clipPath id="playzone-clip"><circle cx="592" cy="522" r="102"/></clipPath>
      <g role="img" aria-label="Photo of children relaxing in the play zone" clip-path="url(#playzone-clip)">
        <rect x="480" y="410" width="230" height="230" fill="url(#playzone-tone)"/>
      </g>

      <circle cx="582" cy="728" r="110" fill="var(--white)"/>
      <clipPath id="rink-clip"><circle cx="582" cy="728" r="104"/></clipPath>
      <g role="img" aria-label="Photo of a girl roller skating on the rink" clip-path="url(#rink-clip)">
        <rect x="470" y="615" width="230" height="230" fill="url(#rink-tone)"/>
      </g>

      <!-- booking bar -->
      <rect x="50" y="853" width="617" height="40" rx="14" fill="var(--red)"/>
      <path d="M64,853 H519 V893 H64 Q50,893 50,879 V867 Q50,853 64,853 Z" fill="var(--royal)"/>
      <text class="booking" x="60" y="878">FIELD TRIPS ARE FUN, UNIQUE AND ENGAGING AND CAN BE BOOKED ONLINE</text>
      <text class="booking" x="524" y="878">AT BRINDLEWAVEFUN.COM</text>
    </svg>
  </div>
</div>
</body>
</html>
```